Accountant website

Please design a accountant website for www.quillbrookadvisory.com.au. This site is majorly out of date, and is not supported by modern browsers.

The style should use the reds from the design at dev.quillbrookadvisory.com.au, and should be modern and make use of Slides (large content slides that the user scrolls through on the front page).

The content is largely already on the site, however happy to move some around to suit the modern design as required.

The dev.quillbrookadvisory.com.au was a rough mock up that I have completed that the client is "happy" with the direction, however this needs a lot of polish and finishing touches, and I will accept designs that differ from this, but highly recommend that this is used as a guide.

Ready to be sliced PSD Only - HTML no required.

In all honesty, although I can technically do a lot of this, the polished finished I want for this site has eluded me in a few attempts, and therefore I am looking out there at you much more artistic people to finish (or redesign if required) this site.

Target Market(s)

Higher end Small - Medium Business

Industry/Entity Type

Accountant

Requirements
Must have
• Must use the logo from dev.quillbrookadvisory.com.au use exactly the red colours as defined in this layout. A basic layout PSD (to get the colour etc) and the logo in ai format is attached to this project. Please ignore the SSL warning on the development site.

The final product does NOT have to be the same as shown on dev.quillbrookadvisory.com.au however the red colour scheme must be used. The client DOES want the logo on the RIGHT.

Must have a front landing page design, and a page layout that considers the other page content (at least one separate PSD)
Nice to have
• I really am looking at a slide format for the front page simular to:

http://www.plumvane.com/au/
http://www.tessaform.com/

The attached photos should be used on the site. Was considering a rotating banner with these images are a watermark background on a solid Red header bar, but happy to be shown other options.
Should not have
• Please no "Layout Goblin" submissions.

```html
<!DOCTYPE html>
<html lang="en">
<head>
<meta charset="utf-8">
<title>Quillbrook Advisory</title>
<link href="https://fonts.googleapis.com/css2?family=Oxygen:wght@400;700&family=Play&family=Roboto:wght@400;500&display=swap" rel="stylesheet">
<style>
:root{
  --red:#c0272d;
  --red-bar:#b9282d;
  --ink:#222;
  --body:#333;
  --grey-head:#5f5f5f;
  --pale:#f7f7f7;
  --footer:#262626;
  --white:#fff;
}
*{margin:0;padding:0;box-sizing:border-box}
html,body{width:1018px;height:1200px;overflow:hidden;background:var(--white)}
body{position:relative;font-family:"Roboto",sans-serif;color:var(--body)}
.abs{position:absolute}

/* header */
.site-header{position:absolute;left:0;top:0;width:1018px;height:112px;background:var(--white)}
.brand{position:absolute;right:132px;top:30px;display:flex;align-items:center;gap:8px;font-family:"Oxygen",sans-serif;font-weight:700;font-size:24px;color:var(--ink);letter-spacing:-.3px}
.brand-mark{width:14px;height:14px;background:var(--red)}
.main-nav{position:absolute;left:134px;top:83px;display:flex;gap:19px;font-family:"Oxygen",sans-serif;font-size:12.5px;color:var(--ink)}
.main-nav .active{color:var(--red)}

/* hero */
.hero{position:absolute;left:0;top:112px;width:1018px;height:378px;overflow:hidden}
.hero-photo{position:absolute;inset:0;background:linear-gradient(90deg,#9a9a98 0%,#d8d2cc 22%,#b8373b 45%,#c23339 60%,#a8b3c0 78%,#cfc8c2 100%)}
.contact-hex{position:absolute;left:399px;top:20px;width:219px;height:246px}
.field{position:absolute;left:24px;width:171px;background:var(--white);font-size:9.5px;color:var(--ink);padding:8px 11px}
.go{position:absolute;left:97px;top:191px;width:26px;height:26px;border-radius:50%;background:var(--white);font-size:9.5px;display:flex;align-items:center;justify-content:center;color:var(--ink)}
.hero-band{position:absolute;left:0;top:293px;width:1018px;height:85px;background:rgba(40,40,40,.6);text-align:center;color:var(--white);font-family:"Play",sans-serif}
.hero-title{font-size:38px;line-height:1;margin-top:7px}
.hero-sub{font-size:24px;line-height:1;margin-top:8px}

/* features */
.features{position:absolute;left:0;top:490px;width:1018px;height:316px;background:var(--pale);box-shadow:0 2px 3px rgba(0,0,0,.12)}
.feature{position:absolute;width:360px;height:126px}
.feature svg{position:absolute;left:0;top:0}
.feature-title{position:absolute;left:133px;top:53px;font-family:"Oxygen",sans-serif;font-weight:700;font-size:15px;color:var(--red);white-space:nowrap}
.feature-text{position:absolute;left:133px;top:81px;width:215px;font-size:10.2px;line-height:14px;color:var(--body)}

/* intro */
.intro-heading{position:absolute;left:134px;top:878px;font-family:"Oxygen",sans-serif;line-height:1.2}
.intro-heading .lead{font-size:24px;color:var(--red);font-weight:700}
.intro-heading .name{font-size:24px;color:var(--grey-head);font-weight:700}
.intro-text{position:absolute;left:578px;top:862px;width:304px;font-size:10.2px;line-height:13.8px}
.read-more{position:absolute;right:138px;top:946px;font-size:10.2px;color:var(--red)}

/* footer */
.site-footer{position:absolute;left:0;top:1014px;width:1018px;height:159px;background:var(--footer);color:var(--white)}
.col-title{position:absolute;top:18px;font-family:"Oxygen",sans-serif;font-weight:700;font-size:12px}
.quick-links{position:absolute;left:134px;top:37px;list-style:none;font-size:10px;line-height:17.6px}
.quick-links li::before{content:"•";margin-right:6px;font-size:7px;vertical-align:1px}
.divider{position:absolute;top:42px;width:1px;height:96px;background:linear-gradient(#262626,#8a8a8a,#262626)}
.quote{position:absolute;left:335px;top:42px;width:150px;font-size:10px;line-height:13px}
.quote-mark{position:absolute;left:-9px;top:-4px;font-family:"Play",sans-serif;font-size:20px;color:#888}
.quote-by{position:absolute;left:400px;top:96px;font-size:10px;letter-spacing:1.4px}
.quote-by small{font-size:7px}
.view-all{position:absolute;left:439px;top:126px;font-size:10px}
.social{position:absolute;left:558px;top:42px;list-style:none;font-size:10.2px}
.social li{display:flex;align-items:center;gap:11px;height:26.5px}
.social-dot{width:18px;height:18px;border-radius:50%;background:var(--white)}
.footer-brand{position:absolute;left:713px;top:28px;display:flex;align-items:center;gap:8px;font-family:"Oxygen",sans-serif;font-weight:700;font-size:21px;color:var(--white)}
.footer-brand .brand-mark{width:12px;height:12px;background:var(--white)}
.badge{position:absolute;left:713px;top:88px;width:50px;height:50px;border-radius:50%;background:var(--white)}
.copyright{position:absolute;left:0;top:1173px;width:1018px;height:27px;background:var(--red-bar);color:var(--white);font-size:10px;text-align:center;line-height:27px}
</style>
</head>
<body>

<header class="site-header">
  <nav class="main-nav">
    <span class="active">About Us</span><span>Services</span><span>Working With Us</span><span>Testimonials</span><span>Article Of The Moment</span><span>Client Login</span>
  </nav>
  <div class="brand"><span class="brand-mark"></span>Quillbrook Advisory</div>
</header>

<section class="hero">
  <div class="hero-photo" role="img" aria-label="Photo of the four team members standing in the office in front of a red company sign"></div>
  <div class="contact-hex">
    <svg width="219" height="246" viewBox="0 0 219 246"><polygon points="109.5,14 205,66 205,180 109.5,232 14,180 14,66" fill="#000" stroke="#000" stroke-width="26" stroke-linejoin="round"/></svg>
    <div class="field" style="top:67px;height:30px">Name:</div>
    <div class="field" style="top:105px;height:29px">Email:</div>
    <div class="field" style="top:142px;height:39px">Message:</div>
    <div class="go">GO</div>
  </div>
  <div class="hero-band">
    <h1 class="hero-title">Business can be hard</h1>
    <p class="hero-sub">But we make detailed analysis of your finances easy</p>
  </div>
</section>

<svg width="0" height="0" class="abs">
  <defs>
    <linearGradient id="g-sky" x1="0" y1="0" x2="0" y2="1"><stop offset="0" stop-color="#c9d6e4"/><stop offset=".6" stop-color="#7d8fa3"/><stop offset="1" stop-color="#2a2f36"/></linearGradient>
    <linearGradient id="g-paper" x1="0" y1="0" x2="1" y2="1"><stop offset="0" stop-color="#f4f4f4"/><stop offset=".7" stop-color="#bfc2c6"/><stop offset="1" stop-color="#5c5f63"/></linearGradient>
    <linearGradient id="g-light" x1="0" y1="0" x2="1" y2="1"><stop offset="0" stop-color="#f5f6f7"/><stop offset=".5" stop-color="#9aa0aa"/><stop offset="1" stop-color="#eef0f2"/></linearGradient>
    <linearGradient id="g-warm" x1="0" y1="0" x2="1" y2="1"><stop offset="0" stop-color="#e0b07a"/><stop offset=".6" stop-color="#c9864e"/><stop offset="1" stop-color="#a9642f"/></linearGradient>
    <linearGradient id="g-port" x1="0" y1="0" x2="0" y2="1"><stop offset="0" stop-color="#b9c6d2"/><stop offset=".6" stop-color="#b07a58"/><stop offset="1" stop-color="#2a2a2a"/></linearGradient>
  </defs>
</svg>

<section class="features">
  <div class="feature" style="left:133px;top:23px">
    <svg width="114" height="126" role="img" aria-label="Illustration of two silhouetted figures against a cloudy sky"><polygon points="57,4 110,34 110,92 57,122 4,92 4,34" fill="url(#g-sky)" stroke="#e2e2e2" stroke-width="4" stroke-linejoin="round"/></svg>
    <h2 class="feature-title">Believing in the here and now</h2>
    <p class="feature-text">There are many varlations of passages of lorem Ipsum avallable, but the majorlty have alteration in some form.</p>
  </div>
  <div class="feature" style="left:530px;top:23px">
    <svg width="114" height="126" role="img" aria-label="Photo of a fountain pen signing a document"><polygon points="57,4 110,34 110,92 57,122 4,92 4,34" fill="url(#g-paper)" stroke="#e2e2e2" stroke-width="4" stroke-linejoin="round"/></svg>
    <h2 class="feature-title">Monthly Billing</h2>
    <p class="feature-text">There are many varlations of passages of lorem Ipsum avallable, but the majorlty have alteration in some form.</p>
  </div>
  <div class="feature" style="left:133px;top:168px">
    <svg width="114" height="126" role="img" aria-label="Illustration of a businessman running with an hourglass"><polygon points="57,4 110,34 110,92 57,122 4,92 4,34" fill="url(#g-light)" stroke="#e2e2e2" stroke-width="4" stroke-linejoin="round"/></svg>
    <h2 class="feature-title">Your Place, In your time</h2>
    <p class="feature-text">There are many varlations of passages of lorem Ipsum avallable, but the majorlty have alteration in some form.</p>
  </div>
  <div class="feature" style="left:530px;top:168px">
    <svg width="114" height="126" role="img" aria-label="Photo of a support agent wearing a headset"><polygon points="57,4 110,34 110,92 57,122 4,92 4,34" fill="url(#g-warm)" stroke="#e2e2e2" stroke-width="4" stroke-linejoin="round"/></svg>
    <h2 class="feature-title">We will actually call you back</h2>
    <p class="feature-text">There are many varlations of passages of lorem Ipsum avallable, but the majorlty have alteration in some form.</p>
  </div>
</section>

<section>
  <h2 class="intro-heading"><span class="lead">Getting to Know</span><br><span class="name">Quillbrook Advisory</span></h2>
  <svg class="abs" style="left:458px;top:860px" width="93" height="102" role="img" aria-label="Portrait photo of the director by the harbour"><polygon points="46.5,3 90,27 90,75 46.5,99 3,75 3,27" fill="url(#g-port)" stroke="#e2e2e2" stroke-width="3" stroke-linejoin="round"/></svg>
  <p class="intro-text">Quillbrook Advisory aims to service the needs of its clients by focusing on the present rather than reporting on historical figures. We recognise that business owners benefit from regular contact with their accountant. One who undertakes a hands on approach in working with business owners to improve their business.</p>
  <span class="read-more">Read More</span>
</section>

<footer class="site-footer">
  <h3 class="col-title" style="left:134px">Quick Links</h3>
  <ul class="quick-links">
    <li>About Us</li><li>Services</li><li>Working With Us</li><li>Testimonials</li><li>Article Of The Moment</li><li>Client Login</li>
  </ul>
  <span class="divider" style="left:286px"></span>
  <h3 class="col-title" style="left:327px">Testimonials</h3>
  <p class="quote"><span class="quote-mark">“</span>Lorem ipsum dolor sit amet, tetuer adipiscing elit, sed diam nonum sum&nbsp; ipsum Lorem ipsum dolor sit amet,”</p>
  <p class="quote-by">Lorem, <small>Director</small></p>
  <span class="view-all">View All</span>
  <span class="divider" style="left:516px"></span>
  <h3 class="col-title" style="left:558px">Follow Us On</h3>
  <ul class="social">
    <li><span class="social-dot"></span>Townsquare</li>
    <li><span class="social-dot"></span>Chirpline</li>
    <li><span class="social-dot"></span>Circlepost</li>
    <li><span class="social-dot"></span>Workring</li>
  </ul>
  <span class="divider" style="left:673px"></span>
  <div class="footer-brand"><span class="brand-mark"></span>Quillbrook Advisory</div>
  <span class="badge" role="img" aria-label="Professional accreditation badge"></span>
</footer>
<div class="copyright">© 2013 Quillbrook Advisory. All Rights Reserved.</div>

</body>
</html>
```